Business card design needed

I am a small start up business in the mortgage broking industry based in Sydney called 'nest2keys'. I will be providing residential mortgages to first home owners, investors and people looking to refinance. I would like to see designs that use the colors blue, black, and white - same as my logo (see logo design uploaded)

Target Market(s)

My target market is First Home Owners, property investors, and people looking to refinance. The loans I will be providing are for residential property only at this stage, and my clients will predominantly be in the 30-50yr age bracket.

Industry/Entity Type

Residential

Contact Information for Business Card

Owen Presley
Director/Mobile Mortgage Broker
nests2keys
PO BOX 2984
West Calder NSW 2175
Mb: 0471 286 904
email: owen@brickvaleplex.com.au

Requirements
Must have
• please use lower case for business name (i.e. nests2keys)

```html
<!DOCTYPE html>
<html lang="en">
<head>
<meta charset="utf-8">
<title>nests2keys – Business Card</title>
<link rel="stylesheet" href="https://fonts.googleapis.com/css2?family=Didact+Gothic&family=Montserrat:wght@700&family=Arimo&display=swap">
<style>
  :root {
    --card-bg: #ffffff;
    --ink: #111111;
    --accent-blue: #4fd0f2;
  }
  html, body {
    margin: 0;
    padding: 0;
    width: 1200px;
    height: 741px;
    overflow: hidden;
    background: var(--card-bg);
  }
  .card {
    position: relative;
    width: 1200px;
    height: 741px;
    background: var(--card-bg);
    color: var(--ink);
  }
  .brand-vertical {
    position: absolute;
    left: 178px;
    top: 163px;
    height: 404px;
    writing-mode: vertical-rl;
    transform: rotate(180deg);
    font-family: "Didact Gothic", sans-serif;
    font-size: 58px;
    line-height: 1;
    color: var(--ink);
    text-align: center;
    white-space: nowrap;
  }
  .divider {
    position: absolute;
    left: 268px;
    top: 163px;
    width: 8px;
    height: 404px;
    background: var(--accent-blue);
  }
  .details {
    position: absolute;
    left: 0;
    top: 0;
  }
  .details > * {
    position: absolute;
    margin: 0;
    line-height: 1;
    white-space: nowrap;
    left: 302px;
  }
  .business-name {
    top: 232px;
    font-family: "Montserrat", sans-serif;
    font-weight: 700;
    font-size: 80px;
    letter-spacing: 1px;
  }
  .person-name {
    top: 312px;
    font-family: "Didact Gothic", sans-serif;
    font-size: 62px;
  }
  .person-role {
    top: 376px;
    font-family: "Didact Gothic", sans-serif;
    font-size: 44px;
  }
  .postal {
    top: 421px;
    font-family: "Arimo", sans-serif;
    font-size: 23px;
  }
  .mobile {
    top: 453px;
    left: 304px;
    font-family: "Arimo", sans-serif;
    font-size: 28px;
  }
  .email {
    top: 486px;
    left: 306px;
    font-family: "Arimo", sans-serif;
    font-size: 27px;
  }
</style>
</head>
<body>
  <main class="card">
    <div class="brand-vertical">nests2keys</div>
    <div class="divider"></div>
    <section class="details">
      <h1 class="business-name">nests2keys</h1>
      <p class="person-name">Owen Presley</p>
      <p class="person-role">Director/Mobile Mortgage Broker</p>
      <p class="postal">PO BOX 2984 West Calder NSW 2175</p>
      <p class="mobile">Mb: 0471•286•904</p>
      <p class="email">email: owen@brickvaleplex.com.au</p>
    </section>
  </main>
</body>
</html>
```